Now Leasing Banner

Looking for a banner that says the following information approx 4' x 30'

Now Leasing Maple Ridge Court 925-318-6042

Target Market(s)

Drive by traffic

Industry/Entity Type

Residential property management

Requirements
Must have
• Clear and readable from a distance

```html
<!DOCTYPE html>
<html lang="en">
<head>
<meta charset="utf-8">
<title>Now Leasing Banners – Maple Ridge Court</title>
<link rel="stylesheet" href="https://fonts.googleapis.com/css2?family=Bebas+Neue&family=Oswald:wght@500;600&display=swap">
<style>
  :root {
    --backdrop: #e9e7e3;
    --banner-red: #d9321a;
    --banner-red-deep: #c02a14;
    --banner-black: #151515;
    --banner-blue: #0e4fa9;
    --accent-yellow: #f7e600;
    --text-white: #ffffff;
    --line-dark: #1a1a1a;
  }
  * { margin: 0; padding: 0; box-sizing: border-box; }
  html, body {
    width: 1200px;
    height: 1200px;
    overflow: hidden;
    background: var(--backdrop);
  }
  .banner-set {
    position: relative;
    width: 1200px;
    height: 1200px;
  }
  .banner {
    position: absolute;
    top: 85px;
    width: 138px;
    height: 1028px;
    overflow: hidden;
    background: var(--banner-color);
  }
  .banner--red { left: 254px; --banner-color: var(--banner-red); --dot-ring: var(--line-dark);
    background: linear-gradient(180deg, var(--banner-red) 0%, var(--banner-red-deep) 100%); }
  .banner--black { left: 484px; --banner-color: var(--banner-black); --dot-ring: var(--text-white); }
  .banner--blue { left: 714px; --banner-color: var(--banner-blue); --dot-ring: var(--accent-yellow); }

  .property-name {
    position: absolute;
    top: 52px;
    left: 0;
    width: 100%;
    text-align: center;
    font-family: "Oswald", sans-serif;
    font-weight: 600;
    font-size: 22px;
    line-height: 1.12;
    color: var(--accent-yellow);
    text-transform: uppercase;
  }
  .property-phone {
    position: absolute;
    top: 132px;
    left: 0;
    width: 100%;
    text-align: center;
    font-family: "Oswald", sans-serif;
    font-weight: 500;
    font-size: 17px;
    color: var(--text-white);
  }
  .feature-art {
    position: absolute;
    top: 180px;
    left: -70px;
    width: 278px;
    height: 290px;
  }
  .leasing-word {
    position: absolute;
    left: 69px;
    top: 688px;
    transform: translate(-50%, -50%) rotate(-90deg);
    font-family: "Bebas Neue", sans-serif;
    font-size: 142px;
    line-height: 1;
    letter-spacing: 1px;
    color: var(--text-white);
    white-space: nowrap;
  }
  .now-word {
    position: absolute;
    top: 888px;
    left: 0;
    width: 100%;
    text-align: center;
    font-family: "Bebas Neue", sans-serif;
    font-size: 76px;
    line-height: 1;
    color: var(--accent-yellow);
  }
</style>
</head>
<body>
<main class="banner-set">

  <section class="banner banner--red">
    <h2 class="property-name">Maple Ridge<br>Court</h2>
    <p class="property-phone">925-318-6042</p>
    <svg class="feature-art" viewBox="0 0 278 290" aria-hidden="false">
      <path d="M10 52 A132 132 0 0 1 268 52" fill="none" stroke="var(--line-dark)" stroke-width="2"/>
      <circle cx="139" cy="138" r="129" fill="var(--accent-yellow)" role="img" aria-label="Playful yellow circle filled with hand-drawn geometric doodles"/>
      <circle cx="133" cy="278" r="21" fill="var(--banner-color)" stroke="var(--dot-ring)" stroke-width="3"/>
    </svg>
    <p class="leasing-word">Leasing</p>
    <p class="now-word">Now</p>
  </section>

  <section class="banner banner--black">
    <h2 class="property-name">Maple Ridge<br>Court</h2>
    <p class="property-phone">925-318-6042</p>
    <svg class="feature-art" viewBox="0 0 278 290" aria-hidden="false">
      <circle cx="139" cy="138" r="129" fill="var(--accent-yellow)" role="img" aria-label="Playful yellow circle filled with hand-drawn geometric doodles"/>
      <circle cx="133" cy="278" r="21" fill="var(--banner-color)" stroke="var(--dot-ring)" stroke-width="3"/>
    </svg>
    <p class="leasing-word">Leasing</p>
    <p class="now-word">Now</p>
  </section>

  <section class="banner banner--blue">
    <h2 class="property-name">Maple Ridge<br>Court</h2>
    <p class="property-phone">925-318-6042</p>
    <svg class="feature-art" viewBox="0 0 278 290" aria-hidden="false">
      <path d="M10 52 A132 132 0 0 1 268 52" fill="none" stroke="var(--accent-yellow)" stroke-width="2"/>
      <circle cx="139" cy="138" r="129" fill="var(--accent-yellow)" role="img" aria-label="Playful yellow circle filled with hand-drawn geometric doodles"/>
      <circle cx="133" cy="278" r="21" fill="var(--banner-color)" stroke="var(--dot-ring)" stroke-width="3"/>
    </svg>
    <p class="leasing-word">Leasing</p>
    <p class="now-word">Now</p>
  </section>

</main>
</body>
</html>
```